Electrical contractor Brochure design

We are looking a elegant brochure design for our new branding campaign. Logo ai file is attached. We mainly work in power plants and manufacturing facilities. We would like some pictures to show those types of facilities.

Target Market(s)

Industrial commercial electrician

Industry/Entity Type

Contractor

Font styles to use
Sans Serif

```html
<!DOCTYPE html>
<html lang="en">
<head>
<meta charset="utf-8">
<title>Corwin Electric Brochure</title>
<link href="https://fonts.googleapis.com/css2?family=Open+Sans:wght@400;600;700&display=swap" rel="stylesheet">
<style>
:root{
  --red:#d4202a;
  --red-dark:#b81c25;
  --black:#111111;
  --navy:#1b2240;
  --white:#ffffff;
  --paper:#f4f4f4;
  --bg:#d9d9d9;
  --ink:#222222;
}
*{box-sizing:border-box;margin:0;padding:0}
html,body{width:1200px;height:1200px;overflow:hidden;background:var(--bg);font-family:"Open Sans",Arial,sans-serif;color:var(--ink)}
.spread{position:absolute;left:40px;width:1120px;height:560px;box-shadow:0 6px 18px rgba(0,0,0,.2)}
.spread.outside{top:20px}
.spread.inside{top:615px}
.panel{position:absolute;top:0;width:560px;height:560px;background:var(--white);overflow:hidden}
.panel.left{left:0}
.panel.right{left:560px;background:var(--paper)}
.abs{position:absolute}
.stripe{position:absolute;left:0;width:100%;height:8px;display:flex}
.stripe span{display:block;height:100%}
.logo{position:absolute;display:flex;align-items:center;gap:6px;font-weight:700;color:var(--black);font-size:17px;letter-spacing:.2px}
.logo i{display:block;width:14px;height:14px;border-radius:50%;background:var(--red)}
/* back panel */
.sectors{position:absolute;left:0;top:114px;width:210px;height:336px;background:var(--red);color:var(--white);padding:18px 16px 0 14px}
.sector{display:flex;gap:10px;height:106px;border-bottom:1px solid rgba(255,255,255,.7);margin-bottom:10px}
.sector:last-child{border-bottom:none}
.sector svg{flex:none;margin-top:2px}
.sector h3{font-size:9.5px;font-weight:600;margin-bottom:3px}
.sector p{font-size:7.6px;line-height:1.3;text-align:justify}
.photo{position:absolute}
.contact{position:absolute;left:210px;top:468px;font-size:9px;line-height:1.65;font-weight:600}
.contact li{list-style:none;display:flex;align-items:center;gap:7px}
.contact li b{display:block;width:6px;height:6px;border-radius:50%;background:var(--red)}
.web{position:absolute;right:24px;bottom:14px;color:var(--white);font-size:11px}
.tagline{position:absolute;right:26px;top:470px;text-align:right;font-weight:700;font-size:14px;line-height:1.35;color:var(--black);text-transform:uppercase}
/* inside left */
.about{position:absolute;left:0;top:0;width:560px;height:250px;background:linear-gradient(180deg,#0e1430 0%,#25305a 55%,#141a33 100%);color:var(--white);padding:40px 26px 0 24px}
.heading{display:flex;align-items:center;gap:8px;font-size:24px;font-weight:400;text-transform:uppercase}
.about p{font-size:8.6px;line-height:1.5;margin-top:10px;max-width:500px}
.mission{position:absolute;left:16px;top:270px;width:180px;height:275px;background:var(--red);color:var(--white);padding:62px 12px 0}
.mission::before,.mission::after{content:"";position:absolute;left:0;right:0;height:2px;background:var(--white)}
.mission::before{top:10px}.mission::after{bottom:10px}
.mission h2{font-size:20px;font-weight:400;margin:6px 0 8px}
.mission p{font-size:8.2px;line-height:1.45;text-align:justify}
.services{position:absolute;left:212px;top:262px;width:336px}
.services h2{display:flex;align-items:center;gap:6px;color:var(--red);font-size:20px;font-weight:400}
.services p{font-size:8.4px;line-height:1.4;margin:5px 0 6px}
.services ul{list-style:none;font-size:8.4px;line-height:1.55}
.services li{display:flex;align-items:center;gap:6px}
.services li::before{content:"";border-left:6px solid var(--red);border-top:4px solid transparent;border-bottom:4px solid transparent}
/* inside right */
.proj-head{position:absolute;left:18px;top:28px;display:flex;align-items:center;gap:10px;color:var(--red);font-size:22px;text-transform:uppercase}
.project{position:absolute;left:18px;width:430px;height:84px;background:var(--red);color:var(--white)}
.project .thumb{position:absolute;left:4px;top:4px;width:128px;height:76px;border:2px solid var(--white)}
.project .info{position:absolute;left:146px;top:6px;right:10px;font-size:7.4px;line-height:1.3}
.project h4{font-size:8.6px;font-weight:600;margin-bottom:2px;text-transform:uppercase}
.rule{position:absolute;left:70px;top:470px;width:310px;height:2px;background:var(--black)}
.clients-title{position:absolute;left:0;width:100%;top:482px;text-align:center;color:var(--red);font-size:13px;text-transform:uppercase}
.clients{position:absolute;left:10px;right:10px;top:516px;display:flex;justify-content:space-between;align-items:center;font-size:10px;font-weight:700;color:var(--navy)}
.clients span{display:flex;align-items:center;gap:4px}
.clients i{display:block;width:9px;height:9px;background:var(--red)}
</style>
</head>
<body>

<!-- Outside spread -->
<section class="spread outside">
  <article class="panel left back-cover">
    <div class="stripe" style="top:0"><span style="width:62%;background:var(--red)"></span><span style="width:38%;background:var(--black)"></span></div>
    <div class="abs" style="left:0;top:106px;width:100%;height:8px;background:var(--black)"></div>

    <div class="sectors">
      <div class="sector">
        <svg width="22" height="20" viewBox="0 0 22 20"><rect x="1" y="12" width="4" height="8" fill="#fff"/><rect x="7" y="8" width="4" height="12" fill="#fff"/><rect x="13" y="4" width="4" height="16" fill="#fff"/><path d="M18 0v6M15.5 2.5L18 0l2.5 2.5" stroke="#fff" stroke-width="1.5" fill="none"/></svg>
        <div><h3>INDUSTRIAL</h3><p>Corwin Electric continually strives to meet the electrical needs of industrial customers. Power plants to manufacturing facilities we have you covered.</p></div>
      </div>
      <div class="sector">
        <svg width="22" height="22" viewBox="0 0 22 22"><circle cx="11" cy="11" r="8" stroke="#fff" stroke-width="2" fill="none"/><circle cx="11" cy="11" r="3" fill="#fff"/></svg>
        <div><h3>COMMERCIAL</h3><p>From banks to retail stores to corporate offices. We have done them all, and we welcome the opportunity to service your needs as well.</p></div>
      </div>
      <div class="sector">
        <svg width="22" height="22" viewBox="0 0 22 22"><circle cx="8" cy="12" r="6" stroke="#fff" stroke-width="3" stroke-dasharray="3 2" fill="none"/><circle cx="17" cy="5" r="3.5" stroke="#fff" stroke-width="2" fill="none"/></svg>
        <div><h3>INSTITUTIONAL</h3><p>We have the experience you have come to expect for the construction of educational, health care and public service facilities, as well as major renovation projects in these fields.</p></div>
      </div>
    </div>

    <div class="photo" role="img" aria-label="Industrial refinery lit at dusk, seen in red tones" style="left:210px;top:114px;width:350px;height:336px;background:linear-gradient(180deg,#2a0a0a 0%,#7a1a14 45%,#3a0d0b 80%,#140506 100%)"></div>

    <div class="logo" style="left:40px;top:492px"><i></i>Corwin Electric</div>
    <ul class="contact">
      <li><b></b>1180 Harbor Ridge Rd, Lindale KY 41000</li>
      <li><b></b>555-010-0006</li>
      <li><b></b>555-010-0393</li>
      <li><b></b>info@corwin-electric.com</li>
      <li><b></b>www.corwin-electric.com</li>
    </ul>
    <div class="stripe" style="bottom:0"><span style="width:55%;background:var(--red)"></span><span style="width:45%;background:var(--black)"></span></div>
  </article>

  <article class="panel right front-cover" style="background:var(--white)">
    <div class="stripe" style="top:0;background:var(--black)"></div>
    <div class="logo" style="left:180px;top:50px;font-size:20px"><i style="width:18px;height:18px"></i>Corwin Electric</div>
    <svg class="abs" style="left:0;top:100px" width="560" height="360" viewBox="0 0 560 360" aria-hidden="true">
      <polygon points="0,24 560,8 560,20 0,36" fill="var(--red)"/>
    </svg>
    <div class="photo" role="img" aria-label="Power plant with tall stacks at sunset" style="left:0;top:132px;width:560px;height:318px;background:linear-gradient(180deg,#e58a3a 0%,#6b2a1a 30%,#2a120c 60%,#0d0706 100%)">
      <span class="web">www.corwin-electric.com</span>
    </div>
    <svg class="abs" style="left:0;top:440px" width="560" height="30" viewBox="0 0 560 30" aria-hidden="true">
      <polygon points="200,10 560,0 560,14 180,22" fill="var(--red)"/>
    </svg>
    <p class="tagline">The premier provider<br>of electrical contracting in the Ohio Valley</p>
    <div class="stripe" style="bottom:0;background:var(--black)"></div>
  </article>
</section>

<!-- Inside spread -->
<section class="spread inside">
  <article class="panel left">
    <div class="about" role="img" aria-label="Night view of an industrial plant in deep blue tones">
      <h2 class="heading"><svg width="18" height="22" viewBox="0 0 18 22"><circle cx="9" cy="6" r="5" fill="#fff"/><rect x="1" y="13" width="16" height="9" rx="2" fill="#fff"/></svg>About Us</h2>
      <p>Corwin Electric has been serving the Kentucky, Ohio and Indiana regions since 2004. We serve the Industrial and Commercial markets. Corwin Electric currently holds license for the states of Kentucky and Ohio. These license easily reciprocate to other surrounding states.</p>
      <p>Corwin Electric, LLC is owned and operated by Daniel Corwin. Daniel holds an Electrical Engineering Degree from the State University. His experience includes the design and installation of electrical systems as well as Engineering and Maintenance in the manufacturing industry.</p>
      <p>You will find that our team will provide you with the experience and professionalism you expect.</p>
    </div>

    <div class="mission">
      <svg width="24" height="24" viewBox="0 0 24 24"><circle cx="12" cy="12" r="10" stroke="#fff" stroke-width="2" fill="none"/><circle cx="12" cy="12" r="5" stroke="#fff" stroke-width="2" fill="none"/><circle cx="12" cy="12" r="1.5" fill="#fff"/></svg>
      <h2>OUR MISSION</h2>
      <p>Corwin Electric's mission is to be the premier provider of electrical contracting in the Ohio Valley and surrounding states. We will continuously strive to provide our clients with value added service by providing a safe, challenging, and rewarding environment for our team, which in turn motivates them to take pride in establishing a successful partnership with our many clients throughout our marketplace.</p>
    </div>

    <div class="services">
      <h2><svg width="18" height="18" viewBox="0 0 18 18"><path d="M2 2L16 16M16 2L2 16" stroke="var(--red)" stroke-width="3"/></svg>SERVICES</h2>
      <p>We pride ourselves in the many services we are able to offer our customers. We not only offer Electrical Construction services but from time to time we will General Contract some projects. We also partner with Corwin Signs to offer complete sign services and installations. Listed below are just a few of the many services we can provide.</p>
      <ul>
        <li>Facility &amp; Plant Maintenance</li>
        <li>Lighting Maintenance – Interior, Exterior and Parking Lot</li>
        <li>Lighting Controls</li>
        <li>Energy Management Systems</li>
        <li>Infrared Scan Inspections of Equipment</li>
        <li>Fire Alarm Systems</li>
        <li>Communication Cabling Systems</li>
        <li>Generators</li>
        <li>New Construction</li>
        <li>Renovation</li>
        <li>Plant Relocation</li>
        <li>Demolition and Removal of Equipment</li>
        <li>Purchase of Surplus Machines and Equipment</li>
        <li>Excavation</li>
      </ul>
    </div>
  </article>

  <article class="panel right" style="background:var(--white)">
    <h2 class="proj-head"><svg width="28" height="24" viewBox="0 0 28 24"><rect x="1" y="1" width="26" height="17" stroke="var(--red)" stroke-width="2" fill="none"/><path d="M5 14l6-6 4 4 7-7" stroke="var(--red)" stroke-width="2" fill="none"/><path d="M14 18v4M8 23h12" stroke="var(--red)" stroke-width="2"/></svg>Our Project</h2>
    <div class="logo" style="left:380px;top:36px;font-size:13px"><i style="width:11px;height:11px"></i>Corwin Electric</div>

    <div class="project" style="top:82px">
      <div class="thumb" role="img" aria-label="Power station with smokestacks" style="background:linear-gradient(180deg,#b9c7d6 0%,#d9dde0 60%,#c9a46a 100%)"></div>
      <div class="info"><h4>Eastridge Power – Ridgeline Station</h4>Location :<br>Lindale, KY<br>Description :<br>Various Projects included: Installation of new emergency generators, Cable installations, Conduit Installations, Lighting installations</div>
    </div>
    <div class="project" style="top:178px">
      <div class="thumb" role="img" aria-label="Water district office building with blue roof and green lawn" style="background:linear-gradient(180deg,#9cc0e4 0%,#c8d8e6 45%,#5f8a3e 70%,#3f6a2a 100%)"></div>
      <div class="info"><h4>Western Valley Water District</h4>Location :<br>Dover, KY<br>Description :<br>Complete electrical installation for new office and lab. Lighting, receptacles and Voice/Data</div>
    </div>
    <div class="project" style="top:274px">
      <div class="thumb" role="img" aria-label="Roadside restaurant LED sign against the sky" style="background:linear-gradient(180deg,#8fb6e0 0%,#c6d9ec 70%,#9a9a9a 100%)"></div>
      <div class="info"><h4>LED Sign</h4>Location :<br>Aberdeen, OH<br>Description :<br>Installation and setup of LED sign. In partner with Corwin Signs (Jim Corwin – Lindale, KY)</div>
    </div>
    <div class="project" style="top:370px">
      <div class="thumb" role="img" aria-label="Automotive parts factory with parking lot" style="background:linear-gradient(180deg,#a9c6e8 0%,#d2dde8 50%,#b5b8ba 75%,#8c8f90 100%)"></div>
      <div class="info"><h4>Kessler Automotive Components</h4>Location :<br>Lindale, KY<br>Description :<br>Various Projects include, Power Distribution, Line Relocations, Demolition of existing manufacturing lines, Bus Rail Installation and Removal, Electronic scale installation along with concrete pits, Various concrete repairs</div>
    </div>

    <div class="rule"></div>
    <h3 class="clients-title">Our Client</h3>
    <div class="clients">
      <span><i></i>Kessler</span>
      <span>Norland</span>
      <span>Birch Hollow</span>
      <span>Valley P&amp;L</span>
      <span>Eastridge Power Co-op</span>
    </div>
  </article>
</section>

</body>
</html>
```